Maple Lantern Business Card

Design of business cards

Target Market(s)

We are aiming as small business owners who need anything from basic business structures, website plans, business processes and quality assurance.

Industry/Entity Type

Business

Colors

Designer to choose colors to be used in the design.

Requirements
Nice to have
• I would prefer one side of the card to use the green from the logo. Prefer to have the same font as the logo.

```html
<!DOCTYPE html>
<html lang="en">
<head>
<meta charset="utf-8">
<title>Maple Lantern Consulting – Business Card</title>
<link href="https://fonts.googleapis.com/css2?family=Questrial&display=swap" rel="stylesheet">
<style>
  :root {
    --backdrop: #ece9e4;
    --card: #ffffff;
    --green: #8cc63f;
    --charcoal: #55575a;
    --ink: #4a4a4a;
    --muted: #7a7a7a;
  }
  * { margin: 0; padding: 0; box-sizing: border-box; }
  html, body { width: 1200px; height: 913px; overflow: hidden; }
  body {
    background: var(--backdrop);
    font-family: "Questrial", "Century Gothic", sans-serif;
    color: var(--ink);
    position: relative;
  }
  .card {
    position: absolute;
    left: 290px;
    width: 620px;
    height: 354px;
    background: var(--card);
    border-radius: 18px;
    overflow: hidden;
    box-shadow: 0 6px 22px rgba(0,0,0,.12);
  }
  .card--front { top: 60px; }
  .card--back { top: 480px; }

  .brand {
    display: flex;
    align-items: center;
    gap: 10px;
    color: var(--green);
    font-size: 22px;
    letter-spacing: .06em;
    text-transform: uppercase;
    line-height: 1.15;
  }
  .brand__dot {
    width: 16px; height: 16px;
    border-radius: 50%;
    background: var(--green);
    flex: none;
  }
  .card--front .brand {
    position: absolute;
    left: 50%; top: 50%;
    transform: translate(-50%, -50%);
    font-size: 26px;
  }
  .card--back .brand {
    position: absolute;
    left: 40px; top: 150px;
    font-size: 17px;
  }

  .person {
    position: absolute;
    right: 40px; top: 44px;
    text-align: right;
  }
  .person__name { color: var(--green); font-size: 20px; }
  .person__title { color: var(--muted); font-size: 13px; margin-top: 2px; }

  .contact {
    position: absolute;
    right: 40px; top: 112px;
    list-style: none;
    font-size: 13px;
    color: var(--ink);
  }
  .contact li {
    display: flex;
    justify-content: flex-end;
    align-items: center;
    gap: 8px;
    margin-bottom: 6px;
  }
  .contact svg { width: 13px; height: 13px; fill: var(--green); }

  .address {
    position: absolute;
    left: 40px; top: 226px;
    width: 240px;
    text-align: right;
    font-style: normal;
    font-size: 14px;
    line-height: 1.35;
  }
  .address__city { color: var(--muted); font-size: 13px; }

  .corner-tab {
    position: absolute;
    right: 0; top: 0;
    width: 22px; height: 30px;
    background: var(--green);
    border-bottom-left-radius: 14px;
  }
  .footer-band {
    position: absolute;
    left: 0; bottom: 0;
    width: 100%; height: 60px;
  }
  .web {
    position: absolute;
    right: 34px; bottom: 18px;
    color: #fff;
    font-size: 13px;
    letter-spacing: .02em;
  }
</style>
</head>
<body>

  <section class="card card--front">
    <div class="brand"><span class="brand__dot"></span><span>Maple Lantern<br>Consulting</span></div>
  </section>

  <section class="card card--back">
    <div class="corner-tab"></div>

    <div class="person">
      <div class="person__name">Dana Whitfield</div>
      <div class="person__title">Founder &amp; CEO</div>
    </div>

    <ul class="contact">
      <li>555.014.2280
        <svg viewBox="0 0 24 24"><path d="M6.6 10.8a15 15 0 0 0 6.6 6.6l2.2-2.2a1 1 0 0 1 1-.25 11.4 11.4 0 0 0 3.6.57 1 1 0 0 1 1 1V20a1 1 0 0 1-1 1A17 17 0 0 1 3 4a1 1 0 0 1 1-1h3.5a1 1 0 0 1 1 1c0 1.25.2 2.45.57 3.57a1 1 0 0 1-.25 1z"/></svg>
      </li>
      <li>info@maplelantern.com
        <svg viewBox="0 0 24 24"><path d="M2 5h20v14H2zm2 2v.5l8 5 8-5V7l-8 5z"/></svg>
      </li>
      <li>www.maplelantern.com
        <svg viewBox="0 0 24 24"><circle cx="12" cy="12" r="10"/></svg>
      </li>
    </ul>

    <div class="brand"><span class="brand__dot"></span><span>Maple Lantern<br>Consulting</span></div>

    <address class="address">
      <div class="address__city">Brookfield</div>
      418 Alder Row, Suite 22<br>
      Brookfield, Ca 90417
    </address>

    <svg class="footer-band" viewBox="0 0 620 60" preserveAspectRatio="none">
      <rect x="0" y="44" width="620" height="16" fill="var(--green)"/>
      <path d="M430 60 L430 40 Q430 6 470 6 L620 6 L620 60 Z" fill="var(--charcoal)"/>
    </svg>
    <div class="web">www.maplelantern.com</div>
  </section>

</body>
</html>
```